Investment Advisor E-Newsletter Banner Design

I need a banner designed for an email newsletter that will be sent monthly to clients and prospects. We want to see designs that are elegant and use our logo well. The banner should be 922x150px and should go well with the www.bhtlwest.com website. Should include Logo and email and phone number.

Target Market(s)

High net worth investors

Number of Pages Required

1 page

Requirements
Must have
• logo, place for email (info@bhtlwest.com) and phone number (555-219-0387), colors and design that work well with www.bhtlwest.com website

```html
<!DOCTYPE html>
<html lang="en">
<head>
<meta charset="utf-8">
<title>Bayhill Trust – Newsletter Banner</title>
<link rel="stylesheet" href="https://fonts.googleapis.com/css2?family=Cormorant+Garamond:wght@500&family=Montserrat:wght@500&display=swap">
<style>
  :root {
    --navy: #2e2f8c;
    --navy-deep: #262878;
    --white: #ffffff;
    --photo-warm: #cdb8a4;
    --photo-light: #ece4dc;
    --photo-deep: #a58a76;
  }
  * { margin: 0; padding: 0; box-sizing: border-box; }
  html, body { width: 1200px; height: 195px; overflow: hidden; background: var(--white); }
  .banner {
    position: relative;
    width: 1200px;
    height: 195px;
    background: var(--white);
    overflow: hidden;
  }
  .contact-band {
    position: absolute;
    left: 0;
    bottom: 0;
    width: 1200px;
    height: 49px;
    background: linear-gradient(90deg, var(--navy-deep), var(--navy));
    display: flex;
    align-items: center;
    padding-left: 28px;
    gap: 38px;
    z-index: 1;
  }
  .family-photo {
    position: absolute;
    left: 540px;
    top: 0;
    width: 660px;
    height: 195px;
    z-index: 2;
    background:
      radial-gradient(ellipse at 62% 62%, var(--photo-warm) 0%, var(--photo-light) 60%),
      linear-gradient(180deg, var(--photo-light), var(--photo-deep));
    -webkit-mask-image: linear-gradient(90deg, transparent 0%, #000 30%);
    mask-image: linear-gradient(90deg, transparent 0%, #000 30%);
  }
  .brand {
    position: absolute;
    left: 36px;
    top: 30px;
    display: flex;
    align-items: center;
    gap: 20px;
    z-index: 3;
  }
  .brand-mark {
    width: 64px;
    height: 64px;
    border-radius: 50%;
    background: var(--navy);
    flex: none;
  }
  .brand-text {
    display: flex;
    flex-direction: column;
    gap: 6px;
    font-family: "Cormorant Garamond", Georgia, serif;
    font-weight: 500;
    color: var(--navy);
  }
  .brand-name { font-size: 40px; line-height: 1; }
  .brand-tagline { font-size: 19px; line-height: 1; padding-left: 2px; }
  .contact-item {
    display: flex;
    align-items: center;
    gap: 12px;
    font-family: "Montserrat", Arial, sans-serif;
    font-weight: 500;
    font-size: 15px;
    letter-spacing: 0.3px;
    color: var(--white);
    text-transform: uppercase;
  }
  .contact-icon { width: 19px; height: 19px; }
</style>
</head>
<body>
  <div class="banner">
    <div class="contact-band">
      <div class="contact-item">
        <svg class="contact-icon" viewBox="0 0 24 24" fill="none" stroke="#ffffff" stroke-width="1.6" stroke-linejoin="round">
          <path d="M5 3h4l2 5-2.5 1.5a11 11 0 0 0 6 6L16 13l5 2v4a2 2 0 0 1-2 2A16 16 0 0 1 3 5a2 2 0 0 1 2-2z"/>
        </svg>
        <span>555-219-0387</span>
      </div>
      <div class="contact-item">
        <svg class="contact-icon" viewBox="0 0 24 24" fill="none" stroke="#ffffff" stroke-width="1.6" stroke-linejoin="round">
          <rect x="2" y="5" width="20" height="14"/>
          <path d="M2 5l10 8 10-8"/>
        </svg>
        <span>info@bhtlwest.com</span>
      </div>
    </div>

    <div class="family-photo" role="img" aria-label="Photo of a smiling family lying on the floor together around a piggy bank"></div>

    <div class="brand">
      <span class="brand-mark"></span>
      <div class="brand-text">
        <span class="brand-name">Bayhill Trust</span>
        <span class="brand-tagline">Management &amp; Research, Inc.</span>
      </div>
    </div>
  </div>
</body>
</html>
```